automatic Real Estate Sales Brochure

Print-out of 3 to 8 pages automatically on a color inkjet printer. Page size A4
All details for my Real Estate Sales Design Project are in attached file.
Here some points:
We have abound 100 real estate objects for sale (houses, flats and pieces of land).
For each item, our system creates automatically a sales documentation, which we print out and hand to the potential buyers after they've visited the object or send it by mail upon request in form of a pdf.
This document should be of 3 to maximum 8 pages.
It should be of a modern design and invite the client to read it.
The information should be clear and quick to find.
If the global look could somehow relate to the look of our web site www.velorancasa.ch, that would be nice.
The company data is there for legal reasons, but it is the agent's phone and mail that the clients should use for contact.
The photos should be of big size (2 by page?) without being distorted nor cut.
Optionally, to save ink and pages, maybe only the first 3-4 photos full size and the rest smaller?

Target Market(s)

will be printed or sent as PDF "on the fly", meaning no pre-printing at a print shop!

Industry/Entity Type

Real Estate

Font styles to use
Sans Serif

Requirements
Must have
• see details in attached file
Should not have
• no edge-to-edge printing
• no double-page printing (A3)

```html
<!DOCTYPE html>
<html lang="fr">
<head>
<meta charset="utf-8">
<title>Veloran Casa – Description</title>
<link href="https://fonts.googleapis.com/css2?family=Open+Sans:wght@400;600;700;800&display=swap" rel="stylesheet">
<style>
  :root {
    --canvas-bg: #e4e4e2;
    --paper: #ffffff;
    --text: #5a5a5a;
    --heading: #4f4f4f;
    --accent: #e30613;
    --footer-bg: #5f5d5b;
    --footer-text: #ffffff;
    --rule: #6a6a6a;
  }
  * { margin: 0; padding: 0; box-sizing: border-box; }
  html, body {
    width: 1200px; height: 1200px; overflow: hidden;
    background: var(--canvas-bg);
    font-family: "Open Sans", Arial, sans-serif;
    color: var(--text);
  }
  .page {
    position: absolute; left: 190px; top: 20px;
    width: 820px; height: 1160px;
    background: var(--paper);
    box-shadow: 0 4px 18px rgba(0,0,0,0.12);
  }
  .agent-header {
    position: absolute; left: 46px; top: 58px; width: 335px;
    font-size: 16px; line-height: 18px;
    padding-bottom: 6px;
    border-bottom: 2px solid var(--rule);
  }
  .agent-header strong { font-weight: 700; color: var(--heading); }
  .brand-name {
    position: absolute; left: 411px; top: 44px; width: 362px;
    font-size: 45px; line-height: 58px; font-weight: 800;
    color: var(--accent); letter-spacing: 0.5px; text-align: right;
    white-space: nowrap;
  }
  .agent-photo {
    position: absolute; left: 47px; top: 147px;
    width: 178px; height: 256px;
    background: linear-gradient(180deg, #f2efed 0%, #cdb3a4 45%, #3b2a24 80%, #1c1a1b 100%);
  }
  .agent-card {
    position: absolute; left: 46px; top: 414px;
    font-size: 16px; line-height: 18.5px; color: var(--accent);
  }
  .agent-card strong { font-weight: 700; }
  .description { position: absolute; left: 267px; top: 130px; width: 506px; }
  .description h1 {
    font-size: 25px; font-weight: 700; color: var(--heading);
    line-height: 34px; padding-bottom: 1px;
    border-bottom: 1.5px solid var(--rule);
  }
  .description-body { margin-top: 25px; font-size: 16.2px; line-height: 22.6px; }
  .description-body p + p { margin-top: 22.6px; }
  .company-footer {
    position: absolute; left: 0; bottom: 0; width: 820px; height: 95px;
    background: var(--footer-bg); color: var(--footer-text);
    font-size: 16px; line-height: 19px;
  }
  .footer-col { position: absolute; top: 30px; }
  .footer-col strong { font-weight: 700; }
  .footer-legal { left: 46px; }
  .footer-web { left: 377px; }
  .footer-phone { left: 631px; }
</style>
</head>
<body>
<main class="page">
  <header>
    <div class="agent-header"><strong>Elena Marchetti</strong><br>marchetti@velorancasa.ch | 079 456 78 12</div>
    <div class="brand-name">VELORAN CASA</div>
  </header>

  <aside>
    <div class="agent-photo" role="img" aria-label="Portrait photo of the agent"></div>
    <div class="agent-card">
      <strong>Elena Marchetti</strong><br>
      marchetti@velorancasa.ch<br>
      079 456 78 12
    </div>
  </aside>

  <section class="description">
    <h1>Description</h1>
    <div class="description-body">
      <p>Venez visiter sans tarder ce bel appartement situé dans un environnement calme et vert tout en étant proche du centre-ville et de toutes les commodités. Il profite de beaux volumes et de pièces de vie très lumineuses. Au 1er étage d'une copropriété soignée, c'est le bien idéal pour un couple ou une famille.</p>
      <p>Cet appartement pourrait aussi convenir comme investissement pour un client souhaitant le louer.</p>
      <p>Il est en bon état d'entretien et se réjouit d'accueillir ses nouveaux propriétaires !</p>
      <p>Il se distribue ainsi :</p>
      <p>Une entrée avec armoire encastrée desserre de part et d'autre la partie jour et la partie nuit. La spacieuse pièce de vie se compose d'une cuisine ouverte entièrement équipée et aménagée s'ouvrant sur le séjour. Il profite d'une exposition optimale. Du séjour, vous avez accès à un agréable balcon qui offre une belle vue dégagée sur un environnement verdoyant.</p>
      <p>La partie nuit offre trois belles chambres, une salle de bains avec baignoire, lavabo, wc ainsi qu'un wc visiteurs.</p>
      <p>Deux places de parc intérieures en sus s'ajoutent à ce bel appartement !</p>
      <p>N'hésitez pas, contactez-moi pour plus d'informations et pour une visite !</p>
    </div>
  </section>

  <footer class="company-footer">
    <div class="footer-col footer-legal"><strong>Veloran Casa Sàrl</strong><br>Chemin des Vignes 7, 1806 Corsier</div>
    <div class="footer-col footer-web">info@velorancasa.ch<br>www.velorancasa.ch</div>
    <div class="footer-col footer-phone">Tél. 021 945 12 30<br>Fax. 021 945 12 31</div>
  </footer>
</main>
</body>
</html>
```